【業務の内容】
建物(鉄筋(鉄骨)コンクリート躯体)の寿命が、あとどれくらい
残っているのか(=寿命)を評価する業務

【なぜこの業務が必要か】
・いまお住まいのマンションの将来計画を考えるために重要な基礎資料
例えば
・「建物寿命は、あと50年以上あるので、しっかりと設備も改修しよう」
・「建物寿命は、あと50年以上あるので、耐震補強を考えよう」
・「建物寿命が20年程度しか残っていないから、延命のための改修をしよう」
・「建物寿命が20年程度しか残っていないから、建替えの検討をしよう」
・残存寿命が長いなら、耐震補強や給排水設備の改修、共用部のリニューアル等を
実施する価値がある、と判断できる

【この業務を推す背景】
・築30年、40年を超える高経年マンションが増えてきている
・首都圏では大地震の確率が30年以内に70%と言われており。1981年以前の旧耐震
基準の建物は、すでに築40年を超えており、耐震補強工事を行うか、建替えるかの
選択を迫られている

【業務の費用(目安・税別)】 ※あくまでも目安
・1棟当たり 基本料金300,000+コア抜き50,000/ヶ所(1フロアあたり1ヶ所)

例)5階建て1棟のマンションの場合
基本料金300,000+(50,000×5ヶ所)=550,000(税別)
【訴求したい事】
・建物の寿命評価に特化しているので、耐震診断等と比べて比較的
安価に実施できる
・短期間で結果が分かる(着手後およそ1か月程度)
・これからマンションにどれだけ維持修繕や改良などの投資するかという
検討をする際の客観的裏付けのある基礎資料になる
・耐用年数は「集合住宅躯体の長期保全評価指針・同付録」(日本建築
学会)の示す算定式を使って算出する

【特に注意・留意すべき事象】
・「寿命が長い」=「安全」ではない
建物耐用年数が長くても、現在の耐震性能基準に達していなければ大地震で
大破・倒壊の危険性がある。躯体寿命と建物の安全性は全く別物
・建物の寿命と設備(給排水管や電気設備など)の寿命は別物
株式会社環創プラン 本社
〒150-0074
東京都渋谷区桜見台7-13-6朝陽ビル
TEL:03-6928-4171(代)
FAX:03-6928-4178

西日本支社
大阪事務所
〒530-0086
大阪府大阪市北区松風町 6-3-18 青葉セントラルビル
TEL:06-6384-2051
FAX:06-6384-2052

西日本支社
広島事務所
〒730-0094
広島県広島市中区千草通3-8-12浜辺ビル5F
TEL:082-517-6820
FAX:082-517-6829
A4
両面
赤系、緑系、水色系
• 高解像度JPG (.jpg)
• イラストレーター形式 (.ai)
使用可能な画像、図(こちらもチラシ作成上に入れてほしいがわかりやすくいじってもらってOKです)、会社ロゴ等全て添付します。

業界関係者ではなく、一般のかた(いわゆる「素人」)が、パッとみてどう感じるだろうか、という
目線で選定しました。
・あまり小難しい印象は与えず、明快なデザイン
・「マンション販売のチラシ」や「水道修理業者」と勘違いされない
というようなところで差がありました。

はじめてこのワークバザールを利用したのですが、このように色々なご提案をいただき、
正直、驚き(もちろん嬉しい方です)でした。
やはりプロにお任せするだけのことがあると痛感し、
我々の業務も同じような驚きをお客様にお届けできるように心がけたいと思います。

この度はご提案いただきまして、誠にありがとうございました。

```html
<!DOCTYPE html>
<html lang="ja">
<head>
<meta charset="utf-8">
<title>マンション向け 建物耐用年数評価</title>
<link href="https://fonts.googleapis.com/css2?family=M+PLUS+Rounded+1c:wght@800;900&family=Noto+Sans+JP:wght@400;500;700;900&display=swap" rel="stylesheet">
<style>
:root{
  --sky-top:#2f8fd8;
  --sky-mid:#7cc4ef;
  --sky-low:#e4f3fc;
  --navy:#123a6b;
  --title-yellow:#ffe93a;
  --accent-orange:#f08a12;
  --label-blue:#1f6fb8;
  --ink:#222;
  --paper:#ffffff;
  --check-red:#d8322b;
  --photo-grey:#b9c4cc;
}
*{margin:0;padding:0;box-sizing:border-box}
html,body{width:846px;height:1200px;overflow:hidden;background:var(--paper)}
body{font-family:"Noto Sans JP",sans-serif;color:var(--ink)}
.flyer{position:relative;width:846px;height:1200px;overflow:hidden;background:var(--paper)}
.hero{position:absolute;left:0;top:0;width:846px;height:750px;
  background:linear-gradient(180deg,var(--sky-top) 0%,var(--sky-mid) 50%,var(--sky-low) 100%)}
.headline{position:absolute;left:0;top:20px;width:100%;text-align:center;
  font-family:"M PLUS Rounded 1c",sans-serif;font-weight:900;color:var(--title-yellow);
  -webkit-text-stroke:10px var(--navy);paint-order:stroke fill;line-height:1.12}
.headline .line1{font-size:62px;display:block}
.headline .line2{font-size:76px;display:block;letter-spacing:2px}
.lead{position:absolute;left:150px;top:200px;width:546px;padding:12px 20px;
  background:rgba(255,255,255,.92);border-radius:8px;text-align:center;
  font-size:18px;font-weight:700;color:var(--navy);line-height:1.6}
.building-photo{position:absolute;left:390px;top:305px;width:456px;height:445px;
  background:linear-gradient(160deg,rgba(238,243,247,.95) 0%,rgba(201,214,223,.9) 55%,rgba(160,178,192,.85) 100%)}
.inspector-illustration{position:absolute;left:50px;top:300px;width:300px;height:420px;
  border-radius:45% 45% 12px 12px;background:linear-gradient(180deg,#f6c873 0%,#f0b46a 35%,#3c6fa8 72%,#2a4f80 100%);opacity:.9}
.company{position:absolute;left:28px;top:768px;width:276px}
.company-name{font-size:26px;font-weight:900;color:var(--ink);margin-bottom:10px;letter-spacing:1px}
.office{font-size:11.5px;line-height:1.5;color:var(--ink);margin-bottom:8px}
.office-label{display:inline-block;background:var(--label-blue);color:#fff;font-weight:700;
  font-size:11px;padding:1px 8px;margin-bottom:2px;border-radius:2px}
.merits{position:absolute;left:318px;top:760px;width:506px}
.merits-title{font-size:23px;font-weight:900;color:var(--accent-orange);
  border-bottom:3px solid var(--accent-orange);padding-bottom:4px;margin-bottom:10px}
.merit-grid{display:grid;grid-template-columns:1fr 1fr;gap:8px 14px}
.merit{display:flex;gap:6px;font-size:11.5px;line-height:1.5;color:var(--ink)}
.merit svg{flex:0 0 16px;margin-top:2px}
.method{position:absolute;left:318px;top:975px;width:506px}
.method-title{font-size:15px;font-weight:900;color:var(--label-blue);margin-bottom:4px}
.method-text{font-size:11.5px;line-height:1.5;margin-bottom:8px}
.method-photos{display:flex;gap:8px}
.core-photo{flex:1;height:90px;background:linear-gradient(135deg,#d3dadf,var(--photo-grey) 60%,#8e9aa3)}
</style>
</head>
<body>
<div class="flyer">
  <section class="hero">
    <h1 class="headline"><span class="line1">マンション向け</span><span class="line2">建物耐用年数評価</span></h1>
    <p class="lead">建物の残りの寿命を知り、いまお住まいのマンションの<br>将来計画を考えるための重要な基礎資料にしませんか？</p>
    <div class="building-photo" role="img" aria-label="青空を背景にした高層マンションの写真"></div>
    <div class="inspector-illustration" role="img" aria-label="ヘルメットをかぶり虫眼鏡とクリップボードを持つ調査員のイラスト"></div>
  </section>

  <section class="company">
    <p class="company-name">株式会社環創プラン</p>
    <div class="office">
      <span class="office-label">本社</span><br>
      〒150-0074<br>東京都渋谷区桜見台7-13-6朝陽ビル<br>
      TEL:03-6928-4171(代)　FAX:03-6928-4178
    </div>
    <div class="office">
      <span class="office-label">西日本支社</span><br>
      大阪事務所<br>〒530-0086<br>大阪府大阪市北区松風町 6-3-18 青葉セントラルビル<br>
      TEL:06-6384-2051　FAX:06-6384-2052
    </div>
    <div class="office">
      <span class="office-label">西日本支社</span><br>
      広島事務所<br>〒730-0094<br>広島県広島市中区千草通3-8-12浜辺ビル5F<br>
      TEL:082-517-6820　FAX:082-517-6829
    </div>
  </section>

  <section class="merits">
    <h2 class="merits-title">建物耐用年数評価のメリット</h2>
    <div class="merit-grid">
      <div class="merit"><svg width="16" height="16" viewBox="0 0 16 16"><rect x="1" y="1" width="14" height="14" fill="none" stroke="var(--check-red)" stroke-width="2"/><path d="M4 8l3 3 6-7" fill="none" stroke="var(--check-red)" stroke-width="2.2"/></svg><span>建物の寿命評価に特化しているので、耐震診断等と比べて比較的安価に実施できます！</span></div>
      <div class="merit"><svg width="16" height="16" viewBox="0 0 16 16"><rect x="1" y="1" width="14" height="14" fill="none" stroke="var(--check-red)" stroke-width="2"/><path d="M4 8l3 3 6-7" fill="none" stroke="var(--check-red)" stroke-width="2.2"/></svg><span>短期間で結果が分かります！（着手後およそ1か月程度）</span></div>
      <div class="merit"><svg width="16" height="16" viewBox="0 0 16 16"><rect x="1" y="1" width="14" height="14" fill="none" stroke="var(--check-red)" stroke-width="2"/><path d="M4 8l3 3 6-7" fill="none" stroke="var(--check-red)" stroke-width="2.2"/></svg><span>これからマンションにどれだけ維持修繕や改良などの投資をするか検討する際の客観的裏付けのある基礎資料になります！</span></div>
      <div class="merit"><svg width="16" height="16" viewBox="0 0 16 16"><rect x="1" y="1" width="14" height="14" fill="none" stroke="var(--check-red)" stroke-width="2"/><path d="M4 8l3 3 6-7" fill="none" stroke="var(--check-red)" stroke-width="2.2"/></svg><span>耐用年数は「集合住宅躯体の長期保全評価指針・同付録」（全国構造技術協議会）の示す算定式を使って算出します！</span></div>
    </div>
  </section>

  <section class="method">
    <h3 class="method-title">【調査方法】</h3>
    <p class="method-text">建物の各階でコア抜き（壁に円筒形の穴を空ける）により試験体を採取し、<br>その検体を調べることで建物のコンクリート躯体寿命を評価します。</p>
    <div class="method-photos">
      <div class="core-photo" role="img" aria-label="コンクリート壁のコア抜き作業の写真"></div>
      <div class="core-photo" role="img" aria-label="採取したコンクリート試験体の写真"></div>
      <div class="core-photo" role="img" aria-label="コア抜き後の壁面の写真"></div>
    </div>
  </section>
</div>
</body>
</html>
```